Brivet Networks, Inc. Website redesign

Revamp the website, it is old and outdated. www.brivetnetworksinc.com

Target Market(s)

Information Technology Consulting and Staffing

Coding

Coded - Design and coding required

Number of Pages Required

5+ page

Colors

Designer to choose colors to be used in the design.

Requirements
Must have
• Outlined text boxes just like from the Hollis.us site. A clean look

```html
<!DOCTYPE html>
<html lang="en">
<head>
<meta charset="utf-8">
<title>Brivet Networks, Inc.</title>
<link href="https://fonts.googleapis.com/css2?family=Montserrat:wght@400;500;600;700;800;900&display=swap" rel="stylesheet">
<style>
:root{
  --brand:#a31b33;
  --brand-dark:#8a1329;
  --ink:#1c1c1c;
  --text:#333;
  --muted:#777;
  --line:#e4e4e4;
  --white:#fff;
  --footer:#0d0c0c;
}
*{box-sizing:border-box;margin:0;padding:0}
html,body{width:1200px;height:2770px;overflow:hidden;background:var(--white)}
body{font-family:'Montserrat',sans-serif;color:var(--text);position:relative}
section,header,footer{position:absolute;left:0;width:1200px}
.abs{position:absolute}

.site-header{top:0;height:84px;background:var(--white);border-bottom:1px solid #eee}
.brand{left:108px;top:24px;font-weight:800;font-size:26px;color:var(--ink);letter-spacing:1px;display:flex;align-items:center;gap:10px}
.brand-mark{width:22px;height:22px;background:var(--brand);display:inline-block}
.nav{top:35px;font-size:12px;color:#777;letter-spacing:.3px}
.nav.active{color:var(--brand)}

.hero{top:84px;height:632px;background:linear-gradient(120deg,#4d6f90 0%,#355a80 40%,#5a7ea0 70%,#8aa6bf 100%)}
.hero-title{left:108px;top:198px;font-weight:900;font-size:40px;line-height:50px;color:var(--white);letter-spacing:.5px}
.hero-text{left:108px;top:318px;width:440px;font-size:12.5px;line-height:20px;color:var(--white)}
.btn{display:block;width:156px;height:48px;background:var(--brand);color:var(--white);font-size:12px;font-weight:500;text-align:center;line-height:46px;border-bottom:4px solid var(--brand-dark);border-radius:2px}
.hero .btn{left:108px;top:394px}

.about{top:716px;height:446px}
.about h2{left:109px;top:120px;width:460px;font-weight:800;font-size:20px;line-height:30px;color:var(--ink)}
.about p{left:109px;top:196px;width:430px;font-size:13px;line-height:20px}
.about .btn{left:108px;top:294px}
.about-photo{left:601px;top:80px;width:492px;height:294px;border-radius:6px;background:linear-gradient(135deg,#8da4b8,#4f6a86 55%,#2d4562)}

.services{top:1162px;height:684px;background:var(--brand);color:var(--white)}
.sec-title{font-weight:800;font-size:20px;letter-spacing:.3px}
.view-more{font-weight:800;font-size:11px;letter-spacing:.3px}
.services .sec-title{left:109px;top:100px}
.services .view-more{right:110px;top:106px}
.services .rule{left:109px;top:146px;width:982px;height:1px;background:rgba(255,255,255,.35)}
.services .intro{left:109px;top:182px;width:945px;font-size:13px;line-height:20px;font-weight:500}
.svc-photo{top:271px;width:309px;height:185px;border-radius:5px}
.svc-title{top:482px;font-weight:700;font-size:15px}
.svc-text{top:514px;width:220px;font-size:13px;line-height:20px;font-weight:500}

.news{top:1846px;height:530px}
.news .sec-title{left:111px;top:98px;color:var(--ink)}
.news .view-more{right:110px;top:104px;color:var(--ink)}
.news .rule{left:109px;top:140px;width:982px;height:1px;background:var(--line)}
.news-card{top:170px;width:310px;height:298px;background:var(--white);box-shadow:0 1px 4px rgba(0,0,0,.09)}
.news-photo{position:absolute;left:0;top:0;width:310px;height:182px}
.news-title{position:absolute;left:24px;top:208px;width:260px;font-weight:700;font-size:13px;line-height:20px;color:var(--ink)}
.news-date{position:absolute;left:24px;top:262px;font-size:9.5px;color:var(--muted);letter-spacing:.3px}

.site-footer{top:2376px;height:394px;background:var(--footer);color:var(--white)}
.foot-title{top:80px;font-weight:800;font-size:14px;letter-spacing:.2px}
.foot-text{top:118px;font-size:12px;line-height:20px;font-weight:500}
.social{left:941px;top:126px;display:flex;gap:20px}
.social span{width:14px;height:14px;border-radius:50%;background:var(--white);display:block}
.foot-brand{left:110px;top:327px;display:flex;align-items:center;gap:14px}
.foot-brand strong{font-weight:800;font-size:18px}
.foot-brand em{font-style:normal;font-size:11px;font-variant:small-caps}
.copyright{right:110px;top:336px;font-size:10px}
</style>
</head>
<body>

<header class="site-header">
  <div class="abs brand"><span class="brand-mark"></span>BRIVET NETWORKS</div>
  <a class="abs nav active" style="left:524px">HOME</a>
  <a class="abs nav" style="left:607px">ABOUT</a>
  <a class="abs nav" style="left:694px">SERVICES</a>
  <a class="abs nav" style="left:797px">STRATEGY</a>
  <a class="abs nav" style="left:901px">IT NEWS</a>
  <a class="abs nav" style="left:996px">CONTACT US</a>
</header>

<section class="hero" role="img" aria-label="Silhouettes of business people in front of a glowing globe with network lines">
  <h1 class="abs hero-title">WELCOME TO<br>BRIVET NETWORKS INC.</h1>
  <p class="abs hero-text">We offer specialized, highly customized technology solutions for our customers located throughout the United States.</p>
  <a class="abs btn">READ MORE</a>
</section>

<section class="about">
  <h2 class="abs">BRINGING THOUGHT LEADERSHIP AND QUALITY TO EVERY PROJECT</h2>
  <p class="abs">Brivet Networks, Inc. is an 8(a) full-service IT consulting company based in the Washington, DC Metro area. We offer specialized, highly customized technology solutions for our customers located throughout the United States.</p>
  <a class="abs btn">READ MORE</a>
  <div class="abs about-photo" role="img" aria-label="Business team meeting around a screen showing analytics"></div>
</section>

<section class="services">
  <h2 class="abs sec-title">OUR SERVICES</h2>
  <a class="abs view-more">VIEW MORE</a>
  <div class="abs rule"></div>
  <p class="abs intro">Brivet Networks, Inc. organizes our Services into four key areas. While these four services can be implemented individually the majority of our projects successfully combine componets from each. Our people and our process is what makes us successful in providing these services...</p>

  <div class="abs svc-photo" style="left:109px;background:linear-gradient(135deg,#c9ced4,#4a5663)" role="img" aria-label="Consultants working together over documents at a table"></div>
  <h3 class="abs svc-title" style="left:109px">TECHNOLOGY CONSULTING</h3>
  <p class="abs svc-text" style="left:109px">Lorem ipsum dolor sit amet, consectetur adipisicing elit, sed do eiusmod tempor.</p>

  <div class="abs svc-photo" style="left:446px;background:linear-gradient(135deg,#2f4f78,#8a9aaa)" role="img" aria-label="Technician working on server rack cabling"></div>
  <h3 class="abs svc-title" style="left:446px">TECHNOLOGY ASSESSMENT</h3>
  <p class="abs svc-text" style="left:446px">Lorem ipsum dolor sit amet, consectetur adipisicing elit, sed do eiusmod tempor.</p>

  <div class="abs svc-photo" style="left:784px;background:linear-gradient(135deg,#e4e8ec,#6f7d8c)" role="img" aria-label="Business people discussing around a laptop in an office"></div>
  <h3 class="abs svc-title" style="left:784px">HARDWARE / SOFTWARE SALES</h3>
  <p class="abs svc-text" style="left:784px">Lorem ipsum dolor sit amet, consectetur adipisicing elit, sed do eiusmod tempor.</p>
</section>

<section class="news">
  <h2 class="abs sec-title">LATEST NEWS</h2>
  <a class="abs view-more">VIEW MORE</a>
  <div class="abs rule"></div>

  <article class="abs news-card" style="left:112px">
    <div class="news-photo" style="background:linear-gradient(135deg,#1b3f9a,#4a7ad0)" role="img" aria-label="Hand pointing at a blue financial data screen"></div>
    <h3 class="news-title">Lorem ipsum dolor sit amet, consectetur.</h3>
    <p class="news-date">SEPTEMBER 05, 2020</p>
  </article>
  <article class="abs news-card" style="left:445px">
    <div class="news-photo" style="background:linear-gradient(135deg,#d8dade,#5c6470)" role="img" aria-label="Colleagues looking at a laptop together"></div>
    <h3 class="news-title">Lorem ipsum dolor sit amet, consectetur.</h3>
    <p class="news-date">SEPTEMBER 04, 2019</p>
  </article>
  <article class="abs news-card" style="left:779px">
    <div class="news-photo" style="background:linear-gradient(135deg,#e6e6e6,#3c4450)" role="img" aria-label="Developers reviewing code on a desktop monitor"></div>
    <h3 class="news-title">Lorem ipsum dolor sit amet, consectetur.</h3>
    <p class="news-date">SEPTEMBER 04, 2018</p>
  </article>
</section>

<footer class="site-footer">
  <h4 class="abs foot-title" style="left:111px">BUSINESS HOURS</h4>
  <p class="abs foot-text" style="left:112px">Opening Days :<br>Monday - Friday : 8 am - 6 pm<br>Saturday : 9 am - 4 pm</p>

  <h4 class="abs foot-title" style="left:443px">QUICK LINKS</h4>
  <p class="abs foot-text" style="left:445px">Home<br>About<br>Services<br>Strategy<br>IT News<br>Contact Us</p>

  <h4 class="abs foot-title" style="left:691px">CONTACT US</h4>
  <p class="abs foot-text" style="left:691px">301-555-0147 (Office)<br>or send us an email.<br>Also you can visit our<br>contact us page.</p>

  <h4 class="abs foot-title" style="left:941px">FOLLOW US</h4>
  <div class="abs social"><span aria-label="Social link"></span><span aria-label="Social link"></span><span aria-label="Social link"></span></div>

  <div class="abs foot-brand"><strong>BRIVET NETWORKS</strong><em>Insight Delivery Growth</em></div>
  <p class="abs copyright">© 2019 Brivet Networks. All rights reserved.</p>
</footer>

</body>
</html>
```